IT Consultancy Website Redesign

We would like to redesign our current website.

We have an overall look/feel we like based on a rendering we have for our homepage. (Attached)

Pages that need to be designed (11 total):

-Homepage

-Overview (not it's own page just a navigation header/drop down title)
-About Us
-Why Choose Varunel
-Our Approach

-Insights (not it's own page just a navigation header/drop down title)
-Insights (Blog)
-Case Studies
-Events

-Services (not it's own page just a navigation header/drop down title)
- Run-State Support

-Industries
-Legal

-Careers
-Contact page

If you have any questions please ask.

Target Market(s)

Fortune 1000 C-suite executives

Industry/Entity Type

It Company

Coding

Coded - Design and coding required

Number of Pages Required

5+ page

Font styles to use
Serif
Sans Serif

Requirements
Must have
• Pages must closely resemble the example provided

```html
<!DOCTYPE html>
<html lang="en">
<head>
<meta charset="utf-8">
<title>Varunel Solutions — IT Strategy and Implementation</title>
<link href="https://fonts.googleapis.com/css2?family=Montserrat:wght@400;500;600;700&family=Open+Sans:wght@400;600&display=swap" rel="stylesheet">
<style>
:root{
  --red:#d7101d;
  --dark:#1f1f1f;
  --ink:#222;
  --body:#444;
  --muted:#777;
  --light:#f4f4f4;
  --white:#fff;
  --head:'Montserrat',sans-serif;
  --text:'Open Sans',sans-serif;
}
*{margin:0;padding:0;box-sizing:border-box}
html,body{width:1200px;height:4626px;overflow:hidden}
body{position:relative;background:var(--white);font-family:var(--text);color:var(--body)}
.abs{position:absolute}
.photo{position:absolute;overflow:hidden}
.btn{position:absolute;background:var(--red);color:var(--white);font-family:var(--head);font-size:15px;font-weight:500;display:flex;align-items:center;justify-content:center;letter-spacing:.3px}
h1,h2,h3,h4{font-family:var(--head);color:var(--ink)}

/* photo tones */
.tone-hero{background:
  radial-gradient(ellipse 22% 35% at 14% 48%,rgba(92,128,170,.85),transparent 70%),
  radial-gradient(ellipse 30% 28% at 30% 12%,rgba(214,220,226,.9),transparent 70%),
  radial-gradient(ellipse 14% 30% at 52% 48%,rgba(150,128,110,.8),transparent 70%),
  radial-gradient(ellipse 18% 32% at 78% 30%,rgba(176,140,115,.75),transparent 70%),
  radial-gradient(ellipse 30% 40% at 80% 80%,rgba(35,48,66,.95),transparent 70%),
  radial-gradient(ellipse 20% 30% at 50% 85%,rgba(225,228,232,.7),transparent 70%),
  linear-gradient(100deg,#6f7c8a 0%,#4b5661 35%,#3a4149 60%,#2b3138 100%)}
.tone-office{background:
  radial-gradient(ellipse 40% 35% at 25% 15%,rgba(208,216,222,.9),transparent 70%),
  radial-gradient(ellipse 18% 30% at 58% 45%,rgba(176,138,110,.8),transparent 70%),
  radial-gradient(ellipse 35% 30% at 50% 75%,rgba(70,90,118,.9),transparent 70%),
  radial-gradient(ellipse 20% 40% at 90% 55%,rgba(48,66,92,.9),transparent 70%),
  linear-gradient(135deg,#7a8591,#44505e 60%,#9aa3ab)}
.tone-team{background:
  radial-gradient(ellipse 40% 30% at 40% 15%,rgba(230,232,234,.9),transparent 70%),
  radial-gradient(ellipse 25% 30% at 30% 60%,rgba(150,120,100,.8),transparent 70%),
  radial-gradient(ellipse 30% 25% at 70% 80%,rgba(200,196,192,.9),transparent 70%),
  radial-gradient(ellipse 15% 15% at 50% 85%,rgba(215,80,80,.5),transparent 70%),
  linear-gradient(135deg,#9a9c9f,#6a6e74 60%,#b9b1ab)}
.tone-notes{background:
  radial-gradient(ellipse 40% 40% at 70% 25%,rgba(240,238,234,.95),transparent 70%),
  radial-gradient(ellipse 25% 25% at 40% 60%,rgba(190,160,140,.7),transparent 70%),
  linear-gradient(135deg,#d9d6d1,#a9a39c)}
.tone-portrait{background:
  radial-gradient(ellipse 45% 30% at 50% 25%,rgba(196,160,138,.85),transparent 70%),
  radial-gradient(ellipse 35% 45% at 30% 40%,rgba(70,50,40,.7),transparent 70%),
  radial-gradient(ellipse 60% 25% at 50% 90%,rgba(230,230,232,.9),transparent 70%),
  linear-gradient(160deg,#c9c6c1,#8a847e)}
.tone-phone{background:
  radial-gradient(ellipse 50% 30% at 50% 30%,rgba(196,158,132,.8),transparent 70%),
  radial-gradient(ellipse 45% 30% at 55% 75%,rgba(240,238,235,.95),transparent 70%),
  radial-gradient(ellipse 30% 25% at 20% 10%,rgba(150,140,132,.8),transparent 70%),
  linear-gradient(160deg,#d6d2cc,#b3aaa1 60%,#c9c3bc)}
.tone-implement{background:
  radial-gradient(ellipse 40% 30% at 55% 25%,rgba(110,110,110,.8),transparent 70%),
  radial-gradient(ellipse 50% 25% at 50% 85%,rgba(80,80,80,.8),transparent 70%),
  linear-gradient(160deg,#3d3d3d,#1f1f1f)}
.tone-assist{background:
  radial-gradient(ellipse 40% 30% at 45% 30%,rgba(120,120,120,.8),transparent 70%),
  radial-gradient(ellipse 50% 30% at 50% 80%,rgba(70,70,70,.8),transparent 70%),
  linear-gradient(160deg,#4a4a4a,#262626)}
.tone-featured{background:
  radial-gradient(ellipse 12% 40% at 38% 55%,rgba(150,150,150,.7),transparent 70%),
  radial-gradient(ellipse 12% 40% at 58% 50%,rgba(120,120,120,.7),transparent 70%),
  radial-gradient(ellipse 15% 35% at 72% 45%,rgba(165,165,165,.6),transparent 70%),
  radial-gradient(ellipse 25% 30% at 50% 90%,rgba(190,190,190,.55),transparent 70%),
  radial-gradient(ellipse 15% 50% at 95% 40%,rgba(40,40,40,.8),transparent 70%),
  linear-gradient(90deg,#5a5a5a 0%,#626262 40%,#454545 100%)}
.tone-legal{background:
  radial-gradient(ellipse 45% 35% at 50% 30%,rgba(70,70,70,.9),transparent 70%),
  radial-gradient(ellipse 45% 30% at 40% 75%,rgba(160,160,160,.7),transparent 70%),
  linear-gradient(160deg,#4a4a4a,#262626)}
.tone-health{background:
  radial-gradient(ellipse 35% 40% at 40% 40%,rgba(200,200,200,.8),transparent 70%),
  radial-gradient(ellipse 35% 25% at 70% 80%,rgba(60,60,60,.8),transparent 70%),
  linear-gradient(160deg,#7a7a7a,#444)}
.tone-manufacture{background:
  radial-gradient(ellipse 20% 12% at 55% 22%,rgba(236,190,40,.95),transparent 70%),
  radial-gradient(ellipse 30% 20% at 52% 38%,rgba(205,160,135,.85),transparent 70%),
  radial-gradient(ellipse 40% 35% at 50% 65%,rgba(60,80,120,.9),transparent 70%),
  radial-gradient(ellipse 30% 40% at 10% 40%,rgba(150,165,185,.8),transparent 70%),
  linear-gradient(160deg,#8895a5,#4d5d73 55%,#9a9ea4)}
.tone-utilities{background:
  radial-gradient(ellipse 25% 15% at 55% 25%,rgba(235,235,235,.9),transparent 70%),
  radial-gradient(ellipse 30% 35% at 40% 60%,rgba(190,190,190,.7),transparent 70%),
  linear-gradient(160deg,#6a6a6a,#333)}
.tone-network{background:
  radial-gradient(ellipse 30% 35% at 50% 25%,rgba(230,230,240,.6),transparent 70%),
  radial-gradient(ellipse 35% 40% at 20% 70%,rgba(150,60,70,.85),transparent 70%),
  radial-gradient(ellipse 35% 40% at 80% 70%,rgba(70,90,140,.85),transparent 70%),
  linear-gradient(135deg,#8a4a52,#4a4d6a 60%,#6f7c9a)}
.tone-laptop{background:
  radial-gradient(ellipse 45% 30% at 40% 15%,rgba(225,230,236,.95),transparent 70%),
  radial-gradient(ellipse 40% 30% at 55% 65%,rgba(170,130,110,.7),transparent 70%),
  radial-gradient(ellipse 40% 30% at 50% 90%,rgba(30,38,48,.9),transparent 70%),
  linear-gradient(135deg,#c7ccd1,#56606c 60%,#2b3138)}
.tone-planning{background:
  radial-gradient(ellipse 18% 15% at 30% 60%,rgba(238,220,80,.9),transparent 70%),
  radial-gradient(ellipse 20% 18% at 70% 70%,rgba(235,140,170,.9),transparent 70%),
  radial-gradient(ellipse 15% 15% at 75% 25%,rgba(200,160,140,.8),transparent 70%),
  radial-gradient(ellipse 35% 30% at 40% 25%,rgba(245,244,240,.95),transparent 70%),
  linear-gradient(135deg,#d6d1ca,#c9c2ba 50%,#b8b2ab)}
.tone-join{background:
  radial-gradient(ellipse 14% 35% at 20% 40%,rgba(60,48,40,.9),transparent 70%),
  radial-gradient(ellipse 12% 25% at 52% 35%,rgba(200,170,120,.85),transparent 70%),
  radial-gradient(ellipse 30% 35% at 60% 55%,rgba(238,236,232,.95),transparent 70%),
  radial-gradient(ellipse 25% 25% at 40% 85%,rgba(225,225,228,.9),transparent 70%),
  radial-gradient(ellipse 20% 40% at 92% 70%,rgba(110,114,120,.9),transparent 70%),
  linear-gradient(100deg,#5a534c 0%,#968e84 35%,#d8d4cf 60%,#a0a2a6 100%)}

/* header */
.site-header{position:absolute;left:0;top:0;width:1200px;height:79px;background:var(--dark)}
.brand-plate{position:absolute;left:0;top:0;width:386px;height:79px;background:var(--white);clip-path:polygon(0 0,386px 0,352px 79px,0 79px)}
.brand{position:absolute;left:144px;top:18px;font-family:var(--head);font-weight:700;font-size:34px;letter-spacing:2px;color:var(--ink);display:flex;align-items:center;gap:10px}
.brand .mark{width:12px;height:12px;background:var(--red)}
.main-nav a{position:absolute;top:31px;font-family:var(--head);font-size:13px;color:var(--white);text-decoration:none;letter-spacing:.3px}
.main-nav a.current{border-bottom:1px solid var(--white);padding-bottom:2px}
.nav-cta{position:absolute;left:927px;top:20px;width:127px;height:39px;border:1px solid #cfcfcf;color:var(--white);font-family:var(--head);font-size:13px;display:flex;align-items:center;justify-content:center}

/* hero */
.hero{position:absolute;left:0;top:79px;width:1200px;height:535px}
.hero-card{position:absolute;left:144px;top:273px;width:388px;height:262px;background:var(--white)}
.hero-card h1{position:absolute;left:28px;top:22px;font-size:42px;line-height:54px;font-weight:600;width:370px}
.hero-card p{position:absolute;left:30px;top:136px;width:340px;font-family:var(--head);font-size:15.5px;line-height:24px;color:var(--ink)}
.slider-prev,.slider-next{position:absolute;left:533px;width:38px;height:38px;display:flex;align-items:center;justify-content:center}
.slider-prev{top:354px;background:var(--dark)}
.slider-next{top:393px;background:var(--red)}

/* empower */
.feature-item{position:absolute;left:648px;width:420px}
.feature-item h4{position:absolute;left:76px;top:0;font-size:19px;font-weight:600;white-space:nowrap}
.feature-item p{position:absolute;left:76px;top:30px;width:330px;font-size:11px;line-height:18px;color:var(--muted)}
.feature-item svg{position:absolute;left:0;top:0}
.dots{position:absolute;background-image:radial-gradient(circle,var(--red) 1px,transparent 1.4px);background-size:8px 8px}
.dots.grey{background-image:radial-gradient(circle,#888 1px,transparent 1.4px)}
.testimonial{position:absolute;left:160px;top:1158px;width:372px;height:166px;background:var(--light)}
.testimonial p{position:absolute;left:136px;top:44px;width:225px;font-size:11px;line-height:20px;color:var(--body)}
.testimonial .who{position:absolute;left:136px;top:110px;font-family:var(--head);font-size:12px;font-weight:600;color:var(--ink)}
.testimonial .role{position:absolute;left:136px;top:129px;font-size:10px;color:var(--red)}

/* services */
.service-card{position:absolute;width:200px}
.service-card span{position:absolute;left:0;width:100%;text-align:center;font-family:var(--head);font-weight:700;font-size:17px;line-height:20px;color:var(--white);text-shadow:0 1px 3px rgba(0,0,0,.45)}

/* section titles */
.section-title{position:absolute;left:0;width:1200px;text-align:center;font-size:38px;font-weight:600}
.title-rule{position:absolute;left:599px;width:2px;background:var(--red)}

.industry-label{position:absolute;width:218px;text-align:center;font-family:var(--head);font-size:23px;color:var(--ink)}
.industry-label.active{color:var(--red)}

.insight{position:absolute;top:3105px;width:298px}
.insight h3{position:absolute;top:218px;left:0;width:305px;font-size:19px;line-height:31px;font-weight:600}
.insight p{position:absolute;top:311px;left:0;width:298px;font-size:10.5px;line-height:18px;color:var(--muted)}
.insight .meta{position:absolute;top:392px;left:2px;font-family:var(--head);font-size:13px;line-height:22px;color:var(--body)}

.join-card{position:absolute;left:666px;top:3861px;width:388px;height:187px;background:rgba(255,255,255,.93);text-align:center}
.join-card h2{margin-top:28px;font-size:38px;font-weight:600}
.join-card p{margin:12px auto 0;width:350px;font-family:var(--head);font-size:15px;line-height:24px;color:var(--ink)}

/* footer */
.site-footer{position:absolute;left:0;top:4249px;width:1200px;height:377px;background:var(--dark);color:var(--white)}
.footer-brand{position:absolute;left:144px;top:60px;font-family:var(--head);font-weight:700;font-size:34px;letter-spacing:2px;color:var(--white);display:flex;align-items:center;gap:10px}
.footer-brand .mark{width:12px;height:12px;background:var(--red)}
.footer-nav a{position:absolute;top:78px;font-family:var(--head);font-size:12px;color:var(--white);text-decoration:none}
.contact-label{position:absolute;top:168px;font-family:var(--head);font-size:11px;display:flex;align-items:center;gap:6px}
.contact-value{position:absolute;top:187px;font-family:var(--head);font-size:16px;font-weight:500;line-height:23px}
.footer-rule{position:absolute;left:0;top:281px;width:1200px;height:1px;background:#3a3a3a}
.copyright{position:absolute;left:144px;top:322px;font-size:11px;color:#bbb}
.to-top{position:absolute;left:1022px;top:313px;width:32px;height:32px;background:var(--red);display:flex;align-items:center;justify-content:center}
</style>
</head>
<body>

<header class="site-header">
  <div class="brand-plate"></div>
  <div class="brand"><span class="mark"></span>VARUNEL</div>
  <nav class="main-nav">
    <a class="current" style="left:418px">OVERVIEW</a>
    <a style="left:522px">OUR FOCUS</a>
    <a style="left:632px">INDUSTRIES</a>
    <a style="left:744px">INSIGHTS</a>
    <a style="left:838px">CAREERS</a>
  </nav>
  <div class="nav-cta">GET IN TOUCH</div>
</header>

<section class="hero">
  <div class="photo tone-hero" role="img" aria-label="Consultants in discussion around a meeting table" style="left:0;top:0;width:1200px;height:535px"></div>
  <div class="hero-card">
    <h1>IT Strategy and Implementation</h1>
    <p>We take your company to the cutting edge of efficiency.</p>
    <div class="btn" style="left:30px;top:196px;width:135px;height:39px">LEARN MORE</div>
  </div>
</section>
<div class="slider-prev"><svg width="12" height="16" viewBox="0 0 12 16"><path d="M9 2 3 8l6 6" fill="none" stroke="#fff" stroke-width="2.5"/></svg></div>
<div class="slider-next"><svg width="12" height="16" viewBox="0 0 12 16"><path d="M3 2l6 6-6 6" fill="none" stroke="#fff" stroke-width="2.5"/></svg></div>

<section class="empower">
  <div class="photo tone-office" role="img" aria-label="Smiling consultant at a desk with a colleague" style="left:144px;top:695px;width:388px;height:260px"></div>
  <div class="photo tone-team" role="img" aria-label="Team working together at a table" style="left:144px;top:966px;width:237px;height:144px"></div>
  <div class="photo tone-notes" role="img" aria-label="Hands writing notes on paper" style="left:392px;top:966px;width:140px;height:144px"></div>
  <div class="dots" style="left:117px;top:1142px;width:132px;height:72px"></div>
  <div class="testimonial">
    <svg class="abs" style="left:137px;top:8px" width="20" height="16" viewBox="0 0 20 16"><path d="M9 2 3 8l6 6M17 2l-6 6 6 6" fill="none" stroke="#d7101d" stroke-width="2"/></svg>
    <p>Information is the lifeblood of every company. Every day, countless data items flow between your employees and systems.</p>
    <div class="who">Dana Whitfield</div>
    <div class="role">Senior Product Manager at Streamvale</div>
  </div>
  <div class="photo tone-portrait" role="img" aria-label="Portrait of a smiling product manager" style="left:144px;top:1158px;width:131px;height:142px"></div>

  <h2 class="abs" style="left:648px;top:680px;font-size:42px;line-height:56px;font-weight:600;width:450px">Empower Digital Transformation</h2>
  <p class="abs" style="left:648px;top:802px;width:400px;font-size:12.5px;line-height:24px;color:var(--body)">Varunel Solutions is a team of IT experts who command the IT field and its related software. From consultancy to implementation, we can help you identify the best solutions for your company and see them through to smooth, constant, and long-lasting operation.</p>

  <div class="feature-item" style="top:966px">
    <svg width="64" height="64" viewBox="0 0 64 64" fill="none" stroke-width="1.8"><rect x="4" y="6" width="56" height="38" stroke="#222"/><rect x="12" y="2" width="40" height="30" stroke="#d7101d"/><path d="M27 12l-5 5 5 5M37 12l5 5-5 5M33 10l-3 14" stroke="#d7101d"/><path d="M2 50h60M10 56h44M24 44v6M40 44v6" stroke="#222"/></svg>
    <h4>Experienced Solution Developers</h4>
    <p>All of our developers have vast experince in the FlowDesk environment.</p>
  </div>
  <div class="feature-item" style="top:1074px">
    <svg width="64" height="64" viewBox="0 0 64 64" fill="none" stroke-width="1.8"><path d="M4 22l12-8 10 4 8-4 12 4 14 12" stroke="#d7101d"/><path d="M6 26l18 18c3 3 6 3 8 1l14-14" stroke="#222"/><path d="M20 34l8 8M26 30l8 8M32 26l8 8" stroke="#222"/><path d="M34 18l-10 8c-2 2 0 5 3 4l8-5" stroke="#d7101d"/></svg>
    <h4>Superior Service Quality</h4>
    <p>Our customers come first and our client retention rate of 98% proves it.</p>
  </div>
  <div class="feature-item" style="top:1182px">
    <svg width="64" height="64" viewBox="0 0 64 64" fill="none" stroke-width="1.8"><path d="M34 8h20v20L26 56 6 36z" stroke="#d7101d"/><circle cx="46" cy="16" r="3" stroke="#222"/><path d="M46 13c2-6 8-8 12-6" stroke="#222"/></svg>
    <h4>Competitive Pricing</h4>
    <p>All solutions are presented with several delivery options e.g full-time US developers, a hybrid of US + near shore.</p>
  </div>
</section>

<section class="services">
  <h2 class="abs" style="left:144px;top:1392px;font-size:42px;line-height:57px;font-weight:600;width:280px">Here’s how we help you</h2>
  <p class="abs" style="left:144px;top:1522px;width:275px;font-size:12.5px;line-height:24px;color:var(--body)">Streamlined, structured data paths allow you to study your company and discover how to make it more efficient, more profitable, and more enduring.</p>
  <div class="dots grey" style="left:814px;top:1404px;width:386px;height:80px"></div>

  <div class="service-card" style="left:445px;top:1410px;height:329px">
    <div class="photo tone-phone" role="img" aria-label="Support specialist on a phone call at a desk" style="left:0;top:0;width:200px;height:291px"></div>
    <span style="top:124px">MANAGED<br>SERVICES</span>
    <div class="btn" style="left:0;top:291px;width:200px;height:38px">READ MORE</div>
  </div>
  <div class="service-card" style="left:650px;top:1458px;height:286px">
    <div class="photo tone-implement" role="img" aria-label="Engineers reviewing work on a laptop" style="left:0;top:0;width:200px;height:286px"></div>
    <span style="top:124px">IMPLEMENTATION<br>SERVICES</span>
  </div>
  <div class="service-card" style="left:855px;top:1505px;height:287px">
    <div class="photo tone-assist" role="img" aria-label="Virtual assistant wearing a headset" style="left:0;top:0;width:200px;height:287px"></div>
    <span style="top:124px">VIRTUAL<br>ASSISTANCE</span>
  </div>
</section>

<section class="featured">
  <div class="photo tone-featured" role="img" aria-label="Project team collaborating around blueprints" style="left:0;top:1873px;width:1200px;height:480px"></div>
  <h2 class="abs" style="left:144px;top:1985px;font-size:42px;line-height:57px;font-weight:600;color:var(--white)">Featured<br>Project</h2>
  <p class="abs" style="left:144px;top:2104px;width:290px;font-size:11.5px;line-height:24px;color:var(--white)">we can help you gain back business momentum and ensure your team has all the FlowDesk support you need to achieve your goals</p>
  <div class="btn" style="left:144px;top:2191px;width:167px;height:40px">VIEW PROJECTS</div>
</section>

<section class="industries">
  <h2 class="section-title" style="top:2426px">Industries</h2>
  <div class="title-rule" style="top:2493px;height:57px"></div>
  <div class="industry-label" style="left:144px;top:2582px">Legal</div>
  <div class="industry-label" style="left:375px;top:2582px">Healthcare</div>
  <div class="industry-label active" style="left:607px;top:2582px">Manufacturing</div>
  <div class="industry-label" style="left:839px;top:2582px">Utilities</div>
  <div class="photo tone-legal" role="img" aria-label="Legal professional signing documents" style="left:144px;top:2622px;width:217px;height:255px"></div>
  <div class="photo tone-health" role="img" aria-label="Doctor working at a laptop" style="left:375px;top:2622px;width:218px;height:255px"></div>
  <div class="photo tone-manufacture" role="img" aria-label="Factory worker in a hard hat" style="left:607px;top:2622px;width:217px;height:255px"></div>
  <div class="photo tone-utilities" role="img" aria-label="Utility engineers in hard hats" style="left:839px;top:2622px;width:217px;height:255px"></div>
</section>

<section class="insights">
  <h2 class="section-title" style="top:2957px">Insights</h2>
  <div class="title-rule" style="top:3023px;height:61px"></div>

  <article class="insight" style="left:144px">
    <div class="photo tone-network" role="img" aria-label="Network of connected people around a cloud" style="left:0;top:0;width:298px;height:192px"></div>
    <h3>Migrating to FlowDesk? Here Are Top 4 Things You Cannot Afford to Ignore</h3>
    <p>FlowDesk is a robust platform that automates, streamlines, and improves the service management processes of your organization, in turn allowing you to deliver superior customer satisfaction.</p>
    <div class="meta">Varunel<br>9 April, 2020</div>
  </article>
  <article class="insight" style="left:451px">
    <div class="photo tone-laptop" role="img" aria-label="Hands typing on a laptop keyboard" style="left:0;top:0;width:298px;height:192px"></div>
    <h3>Highlights from FlowDesk’s Halden Release</h3>
    <p>After Orion, which was released in early 2017, FlowDesk is all set to release Halden. The early access version of the software update was released on November 16, 2017.</p>
    <div class="meta">Varunel<br>9 April, 2020</div>
  </article>
  <article class="insight" style="left:758px">
    <div class="photo tone-planning" role="img" aria-label="Planning session with sticky notes and charts" style="left:0;top:0;width:298px;height:192px"></div>
    <h3>Top 5 Features of FlowDesk’s Latest Orion Release</h3>
    <p>Welcome Orion, FlowDesk’s newest software update. They have made an array of changes to their already superior platform and this series of upgrades have helped make their platform stronger than ever.</p>
    <div class="meta">Varunel<br>9 April, 2020</div>
  </article>
  <div class="btn" style="left:544px;top:3561px;width:112px;height:40px">VIEW ALL</div>
</section>

<section class="join">
  <div class="photo tone-join" role="img" aria-label="Two colleagues reviewing documents at a laptop" style="left:0;top:3682px;width:1200px;height:567px"></div>
  <div class="join-card">
    <h2>Join Varunel</h2>
    <p>We’re always looking to add the finest and brightest talent to our FlowDesk focused team. Available Opportunities</p>
  </div>
  <div class="btn" style="left:794px;top:4030px;width:136px;height:40px">JOIN NOW</div>
</section>

<footer class="site-footer">
  <div class="footer-brand"><span class="mark"></span>VARUNEL</div>
  <nav class="footer-nav">
    <a style="left:512px">OVERVIEW</a>
    <a style="left:603px">OUR FOCUS</a>
    <a style="left:699px">INDUSTRIES</a>
    <a style="left:797px">INSIGHTS</a>
    <a style="left:880px">CAREERS</a>
    <a style="left:973px">GET IN TOUCH</a>
  </nav>
  <div class="contact-label" style="left:144px"><svg width="10" height="10" viewBox="0 0 10 10"><path d="M2 1l2 2-1 1.5c.8 1.6 1.9 2.7 3.5 3.5L8 6l2 2-1.5 1.5C5 9 1 5 .5 1.5z" fill="#fff"/></svg>PHONE</div>
  <div class="contact-value" style="left:144px">555-014-2290</div>
  <div class="contact-label" style="left:404px"><svg width="11" height="9" viewBox="0 0 11 9"><rect x=".5" y=".5" width="10" height="8" fill="#fff"/><path d="M.5.5l5 4 5-4" fill="none" stroke="#1f1f1f"/></svg>EMAIL</div>
  <div class="contact-value" style="left:404px">INFO@VARUNELSOLUTIONS.COM</div>
  <div class="contact-label" style="left:805px"><svg width="8" height="11" viewBox="0 0 8 11"><path d="M4 0a4 4 0 0 1 4 4c0 3-4 7-4 7S0 7 0 4a4 4 0 0 1 4-4z" fill="#fff"/><circle cx="4" cy="4" r="1.5" fill="#1f1f1f"/></svg>ADDRESS</div>
  <div class="contact-value" style="left:805px">418 HARBOR LINE AVE.<br>SUITE 210 LINDEN, VA 20000</div>
  <div class="footer-rule"></div>
  <div class="copyright">Copyright © 2020 Varunel Solutions. All rights reserved.</div>
  <div class="to-top"><svg width="14" height="10" viewBox="0 0 14 10"><path d="M2 8l5-5 5 5" fill="none" stroke="#fff" stroke-width="2.5"/></svg></div>
</footer>

</body>
</html>
```